VANTA SWEEP

Need a professional looking business card that can fit : Name, Title, Cell, and office phone numbers. On the flip side we would like a list of our services : Highway accident management and towing, Crime scene clean up, Illegal drug lab clean up, Drug disposal, and Hazardous materials clean up.

```html
<!DOCTYPE html>
<html lang="en">
<head>
<meta charset="UTF-8">
<title>Vanta Sweep – Business Card</title>
<link rel="stylesheet" href="https://fonts.googleapis.com/css2?family=Merriweather:wght@400;700&family=Open+Sans:wght@400;600&display=swap">
<style>
  :root {
    --navy: #14375e;
    --navy-deep: #0f2d4f;
    --gold: #f2bb12;
    --white: #ffffff;
    --backdrop: #e9e6e1;
    --ink-soft: #1f2f45;
  }
  * { box-sizing: border-box; margin: 0; padding: 0; }
  html, body {
    width: 1200px; height: 1023px; overflow: hidden;
    background: var(--backdrop);
  }
  .canvas {
    position: relative; width: 1200px; height: 1023px;
  }
  .card {
    position: absolute; left: 250px; width: 700px; height: 400px;
    overflow: hidden;
    box-shadow: 0 10px 28px rgba(0,0,0,0.22);
  }

  /* Front */
  .card-front { top: 90px; background: var(--white); }
  .front-accent {
    position: absolute; top: 0; right: 0; width: 110px; height: 26px;
    background: var(--gold);
  }
  .front-band {
    position: absolute; left: 0; right: 0; bottom: 0; height: 44px;
    background: var(--navy);
    border-top: 4px solid var(--gold);
  }
  .brand {
    position: absolute; left: 48px; top: 180px;
    display: flex; align-items: center; gap: 12px;
  }
  .brand-dot {
    width: 40px; height: 40px; border-radius: 50%;
    background: var(--navy);
    flex: none;
  }
  .brand-name {
    font-family: "Merriweather", Georgia, serif;
    font-weight: 700; font-size: 22px; letter-spacing: 1px;
    color: var(--navy); white-space: nowrap;
  }
  .person {
    position: absolute; left: 48px; top: 240px;
  }
  .person-name {
    font-family: "Merriweather", Georgia, serif;
    font-weight: 700; font-size: 40px; color: var(--navy);
    line-height: 1.15;
  }
  .person-title {
    font-family: "Merriweather", Georgia, serif;
    font-weight: 700; font-size: 28px; color: var(--gold);
    margin-left: 150px; line-height: 1.15;
  }
  .contacts {
    position: absolute; right: 50px; top: 48px;
    list-style: none;
    font-family: "Open Sans", Arial, sans-serif;
    font-size: 24px; color: var(--ink-soft);
  }
  .contacts li {
    display: flex; align-items: center; gap: 12px;
    line-height: 1.55; white-space: nowrap;
  }
  .contacts svg { width: 18px; height: 18px; flex: none; }

  /* Back */
  .card-back { top: 540px; background: var(--navy-deep); }
  .back-band {
    position: absolute; top: 0; right: 0; bottom: 0; width: 44px;
    background: var(--gold);
    border-left: 6px solid var(--white);
  }
  .services {
    position: absolute; left: 52px; bottom: 44px;
    font-family: "Merriweather", Georgia, serif;
  }
  .services-heading {
    font-weight: 700; font-size: 22px; color: var(--gold);
    margin-bottom: 6px;
  }
  .services-list { list-style: none; }
  .services-list li {
    display: flex; align-items: center; gap: 14px;
    font-size: 21px; color: var(--white); line-height: 1.55;
  }
  .services-list svg { width: 16px; height: 16px; flex: none; }
</style>
</head>
<body>
<main class="canvas">

  <section class="card card-front" aria-label="Business card front">
    <div class="front-accent"></div>
    <div class="brand">
      <span class="brand-dot"></span>
      <span class="brand-name">VANTA SWEEP</span>
    </div>
    <div class="person">
      <p class="person-name">Marcus</p>
      <p class="person-title">CEO</p>
    </div>
    <ul class="contacts">
      <li>
        <svg viewBox="0 0 18 18" aria-hidden="true"><rect x="4" y="1" width="10" height="16" rx="2" fill="none" stroke="var(--ink-soft)" stroke-width="1.8"/></svg>
        12345 678910
      </li>
      <li>
        <svg viewBox="0 0 18 18" aria-hidden="true"><path d="M4 2c-2 1-2 4 0 7s5 6 8 7c2 0 3-1 3-2l-3-2-2 1c-2-1-3-2-4-4l1-2-2-3z" fill="var(--ink-soft)"/></svg>
        12345 678910
      </li>
      <li>
        <svg viewBox="0 0 18 18" aria-hidden="true"><rect x="1" y="4" width="16" height="11" fill="var(--ink-soft)"/><path d="M1 4l8 6 8-6" fill="none" stroke="var(--white)" stroke-width="1.2"/></svg>
        your@vantasweep.com
      </li>
    </ul>
    <div class="front-band"></div>
  </section>

  <section class="card card-back" aria-label="Business card back">
    <div class="services">
      <p class="services-heading">Our services :</p>
      <ul class="services-list">
        <li><svg viewBox="0 0 20 20" aria-hidden="true"><path d="M10 1l2.6 6 6.4.5-4.9 4.2 1.5 6.3L10 14.6 4.4 18l1.5-6.3L1 7.5 7.4 7z" fill="var(--gold)"/></svg>Highway accident management and towing,</li>
        <li><svg viewBox="0 0 20 20" aria-hidden="true"><path d="M10 1l2.6 6 6.4.5-4.9 4.2 1.5 6.3L10 14.6 4.4 18l1.5-6.3L1 7.5 7.4 7z" fill="var(--gold)"/></svg>Crime scene clean up,</li>
        <li><svg viewBox="0 0 20 20" aria-hidden="true"><path d="M10 1l2.6 6 6.4.5-4.9 4.2 1.5 6.3L10 14.6 4.4 18l1.5-6.3L1 7.5 7.4 7z" fill="var(--gold)"/></svg>Illegal drug lab clean up,</li>
        <li><svg viewBox="0 0 20 20" aria-hidden="true"><path d="M10 1l2.6 6 6.4.5-4.9 4.2 1.5 6.3L10 14.6 4.4 18l1.5-6.3L1 7.5 7.4 7z" fill="var(--gold)"/></svg>Drug disposal, and</li>
        <li><svg viewBox="0 0 20 20" aria-hidden="true"><path d="M10 1l2.6 6 6.4.5-4.9 4.2 1.5 6.3L10 14.6 4.4 18l1.5-6.3L1 7.5 7.4 7z" fill="var(--gold)"/></svg>Hazardous materials clean up</li>
      </ul>
    </div>
    <div class="back-band"></div>
  </section>

</main>
</body>
</html>
```